Business school needs a web design

Who We are:
KRVT is a small business school that offers programs in Project Management. The school is based in West Africa and welcomes students from the whole area. Our aim is to become one of the reference business schools in Africa.

Project Brief:
The site will include all informations relevant for different types of visitors that we have: actual and future students, companies, mass media, future employees, ect. It will present information about subscription, list of programs, presentation of the school and its team,etc.

What We want:
This competition is for Design only no coding! We need design for two pages.
We did some wireframing for the home page and the list of programs page. We made them just to show how we imagine the website would look like. But we encourage creative designs, so you don't have to stick to the wireframe models.

Sites We like:
http://www.ravenmoorcollege.example/
http://www.belvantis.example/fr/etudes.html
http://www.qtl.example/mba/Pages/default.aspx

Color schemes
The logo of the school is red and black. So the color scheme of the website should match that. For the rest, it is opened to your imagination.
Updates

The payment for the project is now garanteed. Good luck to you all !

Target Market(s)

The target market is diversified because we have students of different ages, also company representatives or employees that might visit the website for recruitment purposes. But the majority of our audience should be aged between 20 - 30 years.

Industry/Entity Type

Small Business

Requirements
Must have
• The design must include two pages: a home page and another interior page : might be the list of programs or any other page relevant to the domain. The Home page must include a slide show at the beginning.
The background page must be white.
Nice to have
• The use of flat design for this project is preferred.
The use of Pelican scaffold as a base for the design is an asset.

```html
<!DOCTYPE html>
<html lang="fr">
<head>
<meta charset="utf-8">
<title>KRVT – Accueil</title>
<link href="https://fonts.googleapis.com/css2?family=Open+Sans:wght@400;600&display=swap" rel="stylesheet">
<style>
:root{
  --red:#c8211b;
  --ink:#222;
  --text:#444;
  --muted:#8a8a8a;
  --link:#2a4f9a;
  --line:#dcdcdc;
  --panel:#f0f0f0;
  --slide:#ececec;
  --dark:#3b3b3b;
  --darker:#2e2e2e;
  --date:#6a6a6a;
}
*{box-sizing:border-box;margin:0;padding:0}
html,body{width:822px;height:1200px;overflow:hidden;background:#fff}
body{font-family:'Open Sans',sans-serif;color:var(--text);position:relative}
a{color:inherit;text-decoration:none}
.abs{position:absolute}

/* header */
.brand{left:68px;top:38px;display:flex;align-items:center;gap:6px}
.brand-mark{width:16px;height:16px;background:var(--red)}
.brand-name{font-size:26px;font-weight:600;color:var(--ink);letter-spacing:1px}
.utility{right:70px;top:16px;font-size:9px;color:#666;text-transform:uppercase;display:flex;gap:6px;white-space:nowrap}
.utility span.sep,.mainnav span.sep{color:#bbb}
.mainnav{left:171px;top:59px;width:474px;font-size:9.2px;color:#333;display:flex;justify-content:space-between;white-space:nowrap}
.mainnav .active{color:var(--red)}
.search{left:657px;top:55px;width:96px;height:20px;border:1px solid #ccc;font-size:8.5px;color:#888;padding:3px 8px;background:#fff}
.search svg{position:absolute;right:6px;top:4px}

/* slider */
.slider{left:0;top:107px;width:822px;height:280px;background:var(--slide)}
.slide-photo{left:234px;top:0;width:555px;height:280px;background:linear-gradient(100deg,#e4e6ea 0%,#b9c0c8 40%,#d8dde3 70%,#eef0f2 100%)}
.slide-title{left:68px;top:55px;font-size:17px;line-height:24px;color:var(--ink);width:160px}
.slide-text{left:68px;top:106px;font-size:9px;line-height:13px;color:#555;width:150px}
.slide-btn{left:68px;top:156px;background:#4a4a4a;color:#fff;font-size:9px;padding:4px 8px;border-radius:2px}
.dots{left:69px;top:252px;display:flex;gap:6px}
.dots i{width:10px;height:10px;border-radius:50%;background:#bbb;display:block}
.dots i:first-child{background:#777}

/* side boxes */
.box{border:1px solid var(--line);background:var(--panel)}
.box h3{font-size:12px;font-weight:400;color:var(--red);padding:6px 11px;height:29px;background:#f7f7f7;border-bottom:1px solid var(--line)}
.audience{left:68px;top:401px;width:163px;height:208px}
.audience li{list-style:none;font-size:9px;color:#444;padding:0 11px;height:25px;line-height:25px;border-bottom:1px solid #dedede;margin:0 3px}
.audience li:last-child{border:none}
.tv{left:68px;top:622px;width:163px;height:129px}
.tv-video{position:absolute;left:0;top:29px;width:161px;height:99px;background:linear-gradient(120deg,#9ea4ab,#5f666e)}
.tv-video svg{position:absolute;left:62px;top:30px}
.more-videos{left:69px;top:755px;font-size:9px;color:var(--link)}

/* centre */
.center{left:248px;top:404px;width:327px}
h2{font-size:14px;font-weight:400;color:var(--red)}
.intro{font-size:9px;line-height:16px;color:var(--muted);margin-top:4px}
.rule{height:1px;background:var(--line);margin:14px 0 11px}
.blog{display:flex;gap:13px;margin-top:12px}
.post{width:100px}
.post .ph{height:63px}
.post h4{font-size:9px;font-weight:400;color:var(--ink);margin-top:9px}
.post p{font-size:7.2px;line-height:11.5px;color:var(--muted);margin-top:3px}
.post .meta{font-size:7.4px;color:var(--link);margin-top:3px;line-height:13px}
.post .meta u{display:block}
.event{display:flex;gap:10px;margin-top:12px}
.date{width:44px;height:44px;background:var(--date);color:#fff;text-align:center;font-size:9px;line-height:12px;padding-top:5px;flex:none}
.date b{display:block;font-size:16px;font-weight:600;line-height:20px}
.event h4{font-size:9px;font-weight:400;color:var(--ink)}
.event p{font-size:7.2px;line-height:10.5px;color:var(--muted);margin-top:3px}
.all-events{font-size:9px;color:var(--link);margin-top:12px;display:block}

/* news */
.news{left:590px;top:401px;width:163px;height:515px}
.news-item{display:flex;gap:8px;padding:9px 8px;height:64px;border-bottom:1px solid #dedede}
.news-item .th{width:46px;height:43px;border:2px solid #fff;flex:none}
.news-item h4{font-size:9px;font-weight:400;color:var(--ink)}
.news-item p{font-size:7.4px;line-height:11px;color:var(--muted);margin-top:2px}
.more-news{font-size:9px;color:var(--link);padding:11px 10px}

/* partners */
.partners{left:68px;top:939px;width:685px;border-top:1px solid var(--line);display:flex;justify-content:space-around;align-items:center;height:70px}
.partners span{font-size:14px;font-weight:600;color:#666;display:flex;align-items:center;gap:5px}
.partners i{width:10px;height:10px;background:#999;display:block}

/* footer */
.footer{left:0;top:1008px;width:822px;height:157px;background:linear-gradient(#404040,var(--dark));color:#bbb}
.fcol{position:absolute;top:18px;font-size:8px;line-height:15.5px}
.fcol h5{font-size:10.5px;font-weight:400;color:#fff;margin-bottom:8px}
.fcol .big{font-size:10px;color:#fff;line-height:18px}
.social{display:flex;gap:12px;margin-top:6px}
.social i{width:21px;height:21px;background:#eee;display:block;border-radius:2px}
.phone{display:flex;align-items:center;gap:6px;margin-top:7px}
.email{display:flex;gap:4px;margin-top:8px}
.email span{width:100px;height:19px;background:#fff;color:#888;font-size:8px;padding:3px 10px}
.email i{width:19px;height:19px;border-radius:50%;background:#fff;display:flex;align-items:center;justify-content:center}
.bottom{left:0;top:1165px;width:822px;height:35px;background:var(--darker);color:#999;font-size:9px;text-align:center;line-height:35px}
</style>
</head>
<body>

<header>
  <div class="abs brand"><i class="brand-mark"></i><span class="brand-name">KRVT</span></div>
  <nav class="abs utility"><a>Repertoire du personel</a><span class="sep">/</span><a>Blogue</a><span class="sep">/</span><a>Salle de presse</a><span class="sep">/</span><a>Nous joindre</a><span class="sep">/</span><a>Francais</a></nav>
  <nav class="abs mainnav"><a class="active">A propos de l'KRVT</a><span class="sep">/</span><a>Programmes et Formations</a><span class="sep">/</span><a>Etudiants</a><span class="sep">/</span><a>Nouvelles et Evenements</a><span class="sep">/</span><a>Enterprises</a></nav>
  <div class="abs search">Search
    <svg width="11" height="11" viewBox="0 0 11 11"><circle cx="4.5" cy="4.5" r="3.2" fill="none" stroke="#333" stroke-width="1.6"/><line x1="7" y1="7" x2="10" y2="10" stroke="#333" stroke-width="2"/></svg>
  </div>
</header>

<section class="abs slider">
  <div class="abs slide-photo" role="img" aria-label="Photo of business people shaking hands in an office"></div>
  <h1 class="abs slide-title" style="font-weight:400">Pellentesque habitantmor netus</h1>
  <p class="abs slide-text">Nunc euismod mi purus, id tinci dunt sem porttitor sit amet. Sed in egestas odio.</p>
  <a class="abs slide-btn">Read More</a>
  <div class="abs dots"><i></i><i></i><i></i><i></i></div>
</section>

<aside class="abs box audience">
  <h3>VOUS ETES</h3>
  <ul>
    <li>Futur etudiant</li><li>Etudiant actuel</li><li>Enterprise</li><li>Employeur</li><li>Postulant</li><li>Medias</li><li>Partenaires</li>
  </ul>
</aside>
<aside class="abs box tv">
  <h3>KRVT.TV</h3>
  <div class="tv-video" role="img" aria-label="Video still of a business meeting">
    <svg width="38" height="38" viewBox="0 0 38 38"><circle cx="19" cy="19" r="17" fill="none" stroke="#fff" stroke-width="2.5"/><path d="M15 11 L27 19 L15 27Z" fill="#fff"/></svg>
  </div>
</aside>
<a class="abs more-videos">+ de videos</a>

<main class="abs center">
  <h2>KRVT : devenez les gestionnaires de demain</h2>
  <p class="intro">Nam rhoncus purus at neque fringilla, non eleifend nulla egestas. Nunc elementum aliquet eleifend. Donec rutrum nunc vitae lacus pellentesque facilisis. Phasellus condimentum eros vel felis sagittis tincidunt. Vivamus pellentesque dictum odio, et suscipit nulla posuere sit amet.</p>
  <div class="rule"></div>
  <h2>Blogue</h2>
  <div class="blog">
    <article class="post"><div class="ph" role="img" aria-label="Photo of a team discussing at a desk" style="background:linear-gradient(120deg,#e9e5e0,#a59a8f)"></div><h4>Morbi nisl sapien</h4><p>Nunc euismod mi purus, id tincidunt sem porttitor sit amet. Sed in egestas odio. Suspendisse turpis mi, vehicula sed.</p><div class="meta">Marc Dione<u>Line la suite</u></div></article>
    <article class="post"><div class="ph" role="img" aria-label="Photo of hands working on documents and charts" style="background:linear-gradient(120deg,#d9dee6,#7e8896)"></div><h4>Morbi nisl sapien</h4><p>Nunc euismod mi purus, id tincidunt sem porttitor sit amet. Sed in egestas odio. Suspendisse turpis mi, vehicula sed.</p><div class="meta">Marc Dione<u>Line la suite</u></div></article>
    <article class="post"><div class="ph" role="img" aria-label="Illustration of a blue digital padlock" style="background:linear-gradient(120deg,#1a4d8a,#0c2448)"></div><h4>Morbi nisl sapien</h4><p>Nunc euismod mi purus, id tincidunt sem porttitor sit amet. Sed in egestas odio. Suspendisse turpis mi, vehicula sed.</p><div class="meta">Marc Dione<u>Line la suite</u></div></article>
  </div>
  <div class="rule"></div>
  <h2>Evenements</h2>
  <div class="event"><div class="date">Jan<b>7</b></div><div><h4>Pellentesque habitant</h4><p>Morbi interdum egestas felis, a vestibulum turpis accumsan a. Aliquam sed molestie risus. Mauris dapibus dolor at dui condimentum, in tempus nisi aliquam</p></div></div>
  <div class="event" style="margin-top:20px"><div class="date">Jan<b>7</b></div><div><h4>Pellentesque habitant</h4><p>Morbi interdum egestas felis, a vestibulum turpis accumsan a. Aliquam sed molestie risus. Mauris dapibus dolor at dui condimentum, in tempus nisi aliquam</p></div></div>
  <a class="all-events">Tous les evenements</a>
</main>

<aside class="abs box news">
  <h3>NOUVELLES</h3>
  <div class="news-item"><div class="th" role="img" aria-label="News photo" style="background:linear-gradient(#ccd2d8,#7d8690)"></div><div><h4>Quisque ligula ligula</h4><p>Donec est enim, luctus sed metus quis</p></div></div>
  <div class="news-item"><div class="th" role="img" aria-label="News photo" style="background:linear-gradient(#d6d6d6,#3a3a3a)"></div><div><h4>Quisque ligula ligula</h4><p>Donec est enim, luctus sed metus quis</p></div></div>
  <div class="news-item"><div class="th" role="img" aria-label="News photo" style="background:linear-gradient(#c93a2a,#2d5fb8)"></div><div><h4>Quisque ligula ligula</h4><p>Donec est enim, luctus sed metus quis</p></div></div>
  <div class="news-item"><div class="th" role="img" aria-label="News photo" style="background:linear-gradient(#e6e3dc,#9b9a8c)"></div><div><h4>Quisque ligula ligula</h4><p>Donec est enim, luctus sed metus quis</p></div></div>
  <div class="news-item"><div class="th" role="img" aria-label="News photo" style="background:linear-gradient(#f2f2f2,#5a5552)"></div><div><h4>Quisque ligula ligula</h4><p>Donec est enim, luctus sed metus quis</p></div></div>
  <div class="news-item"><div class="th" role="img" aria-label="News photo" style="background:linear-gradient(#e8e8e8,#3c3f44)"></div><div><h4>Quisque ligula ligula</h4><p>Donec est enim, luctus sed metus quis</p></div></div>
  <div class="news-item"><div class="th" role="img" aria-label="News photo" style="background:linear-gradient(#e8e8e8,#3c3f44)"></div><div><h4>Quisque ligula ligula</h4><p>Donec est enim, luctus sed metus quis</p></div></div>
  <div class="more-news">+ de nouvelles</div>
</aside>

<section class="abs partners">
  <span><i></i>Dealora</span><span>Tallyfold</span><span>Brightmarket</span><span>Corvane</span><span><i></i>Nexapoint</span><span>Thriftbay</span>
</section>

<footer class="abs footer">
  <div class="fcol" style="left:70px"><h5>Suivez-nous</h5><div class="social"><i></i><i></i><i></i><i></i></div></div>
  <div class="fcol" style="left:231px"><h5>A propos</h5>A propose de l'KRVT<br>Admissions<br>Calendrier de L;ecode<br>Offers d'emploi<br>Repertoire du personnel</div>
  <div class="fcol" style="left:359px"><h5>Etudiants</h5>Accueil - Etudiants<br>Programmes et Forma-<br>tions<br>Vie etudiante<div class="big" style="margin-top:6px">Enterprises<br>Blogue</div></div>
  <div class="fcol" style="left:481px;width:130px"><h5>KRVT</h5><p style="line-height:13.5px">12, rue des Acacias Quartier Nord, près du marché central</p>
    <div class="phone" style="margin-top:14px"><svg width="9" height="9" viewBox="0 0 9 9"><path d="M1 1 L3 1 L4 3 L3 4 Q4 6 5 6 L6 5 L8 6 L8 8 Q3 8 1 1Z" fill="#bbb"/></svg>(000) 55 120 40 18</div>
    <div class="phone" style="margin-top:10px"><svg width="9" height="9" viewBox="0 0 9 9"><path d="M1 1 L3 1 L4 3 L3 4 Q4 6 5 6 L6 5 L8 6 L8 8 Q3 8 1 1Z" fill="#bbb"/></svg>(000) 55 931 27 06</div></div>
  <div class="fcol" style="left:631px;width:130px"><h5>Infolettre</h5><p style="line-height:13px">Morbi interdum egestas felis, a vestibulum turpis accumsan a. Aliquam sed molestie risus. condimentum.</p>
    <div class="email"><span>Email ID</span><i><svg width="6" height="7" viewBox="0 0 6 7"><path d="M0 0 L6 3.5 L0 7Z" fill="#333"/></svg></i></div></div>
</footer>
<div class="abs bottom">Copyright &copy; 2014 KRVT. All rights reserved.</div>

</body>
</html>
```